Business and Discussion forum website

I have long been an admirer of a good and professional business forum. Http://lanternbazaar.com got my attention and i am looking for a similar website to it. Basically, my website is going to discuss business, politics, entertainment and social issues. The website should be youthful and captivating. Users should be able to post threads, comments on threads, like and dislike comments. The administrator of the website will be able to delete post/threads. Users should be able to add each other as friends and subsequently be able to message/inbox each other. These are the basic stuffs the website should possess.

Industry/Entity Type

Business

Coding

Coded - Design and coding required

```html
<!DOCTYPE html>
<html lang="en">
<head>
<meta charset="utf-8">
<title>Corvana Forums</title>
<link href="https://fonts.googleapis.com/css2?family=Open+Sans:wght@400;600&family=Ubuntu:wght@400;500;700&display=swap" rel="stylesheet">
<style>
:root{
  --blue:#0a8fd6;
  --nav:#545454;
  --nav-line:#3f3f3f;
  --text:#555;
  --heading:#333;
  --orange:#f7941d;
  --band:#ebebeb;
  --rule:#dcdcdc;
  --white:#fff;
}
*{box-sizing:border-box;margin:0;padding:0}
html,body{width:890px;height:1200px;overflow:hidden;background:var(--white)}
body{position:relative;font-family:"Open Sans",Arial,sans-serif;color:var(--text)}
.topline{position:absolute;left:0;top:0;width:890px;height:4px;background:var(--blue)}

.brand{position:absolute;left:74px;top:26px;display:flex;align-items:center;gap:10px}
.brand-mark{width:40px;height:40px;border-radius:50%;background:var(--blue)}
.brand-name{font-family:"Ubuntu",sans-serif;font-weight:400;font-size:27px;color:#6b6b6b}

.social{position:absolute;right:75px;top:31px;display:flex;align-items:center;gap:5px;font-size:9px;color:#444}
.social-label{margin-right:2px}
.social-dot{width:25px;height:25px;border-radius:50%}
.dot-a{background:#1f6fb8}.dot-b{background:#1c7fa3}.dot-c{background:#d7262c}.dot-d{background:#333}.dot-e{background:#49b6e9}

.nav{position:absolute;left:74px;top:83px;width:743px;height:41px;background:var(--nav);display:flex;align-items:stretch;border-bottom:1px solid #333}
.nav a{color:#eee;text-decoration:none;font-size:9.5px;display:flex;align-items:center;justify-content:center;border-right:1px solid var(--nav-line)}
.nav a:nth-child(1){width:80px}.nav a:nth-child(2){width:100px}.nav a:nth-child(3){width:94px}
.nav a:nth-child(4){width:87px}.nav a:nth-child(5){width:122px}.nav a:nth-child(6){width:95px}
.search{position:absolute;right:7px;top:9px;width:148px;height:23px;border:1px solid #6d6d6d;background:#4c4c4c;font-size:8px;color:#888;padding:0 9px;display:flex;align-items:center;justify-content:space-between}

.hero{position:absolute;left:74px;top:130px;width:743px;height:311px;display:flex;box-shadow:0 18px 14px -12px rgba(0,0,0,.35)}
.hero-media{position:relative;width:495px;height:100%;background:linear-gradient(160deg,#5a5a5a 0%,#2b2622 35%,#3a2418 60%,#141414 100%)}
.hero-title{position:absolute;left:32px;top:222px;color:var(--white);font-size:26px;font-weight:600}
.hero-sub{position:absolute;left:34px;top:257px;color:var(--white);font-size:20px;font-weight:400}
.hero-arrows{position:absolute;right:8px;bottom:10px;display:flex;gap:2px}
.hero-arrows span{width:18px;height:18px;background:#333;display:flex;align-items:center;justify-content:center}
.hero-about{width:248px;background:var(--blue);color:var(--white);padding:42px 30px 0 39px}
.about-title{font-family:"Ubuntu",sans-serif;font-weight:700;font-size:24px;letter-spacing:.5px}
.about-name{font-size:21px;font-weight:400;margin-top:4px;margin-bottom:14px}
.about-text{font-size:9.2px;line-height:17px;margin-bottom:17px}

.welcome{position:absolute;left:74px;top:486px;width:743px;text-align:center}
.welcome h1{font-family:"Ubuntu",sans-serif;font-weight:500;font-size:16px;color:var(--heading);margin-bottom:10px}
.welcome p{font-size:8.8px;line-height:19px;padding:0 12px}

.categories{position:absolute;left:74px;top:593px;display:flex;gap:22px}
.category{width:169px}
.cat-media{height:130px;border-bottom:3px solid var(--blue)}
.m-business{background:linear-gradient(120deg,#d2dbe3,#7a8896 50%,#3f4a55)}
.m-politics{background:linear-gradient(160deg,#e7d7c8,#8a6a5a 55%,#5a4a6a)}
.m-entertain{background:linear-gradient(150deg,#6b4a38,#a78467 50%,#3a2c24)}
.m-social{background:linear-gradient(160deg,#f4e0a8,#d59a4c 50%,#6d4a2a)}
.cat-title{font-family:"Ubuntu",sans-serif;font-weight:500;font-size:13px;color:var(--blue);margin:17px 0 7px}
.cat-list{list-style:none;width:157px}
.cat-list li{height:31.6px;border-bottom:1px solid var(--rule);display:flex;align-items:center;gap:6px;font-size:8.8px;color:#555}
.bullet{width:7px;height:7px;border-radius:50%;background:var(--orange);position:relative;flex:none}
.bullet::after{content:"";position:absolute;left:2px;top:2px;width:2px;height:2px;border-right:1px solid #fff;border-top:1px solid #fff;transform:rotate(45deg)}
.view-more{display:block;width:157px;text-align:right;font-size:9px;color:var(--orange);margin-top:13px}

.band{position:absolute;left:0;top:992px;width:890px;height:160px;background:var(--band);border-bottom:1px solid #ddd}
.band h2{position:absolute;top:24px;width:100%;text-align:center;font-family:"Ubuntu",sans-serif;font-weight:500;font-size:14px;color:var(--blue)}
.band-arrow{position:absolute;top:73px;font-size:10px;color:#aaa}
.feature{position:absolute;top:66px;display:flex;gap:14px}
.feature-thumb{width:78px;height:69px;border:3px solid var(--white);outline:1px solid #ccc}
.t-1{background:linear-gradient(135deg,#d8d0c4,#7d6f63)}
.t-2{background:linear-gradient(135deg,#1b2a7a,#3e5cd0 50%,#0c1230)}
.t-3{background:linear-gradient(135deg,#c2a48a,#6a5344)}
.t-4{background:linear-gradient(135deg,#d7d7d7,#6a6a6a 60%,#2b2b2b)}
.feature h3{font-family:"Ubuntu",sans-serif;font-weight:500;font-size:11px;color:var(--blue);margin-top:-2px}
.feature p{font-size:7.8px;line-height:14px;color:#555;margin:3px 0 6px}
.btn{display:inline-block;background:var(--orange);color:var(--white);font-size:6.5px;padding:5px 10px;border:1px solid #e3820e}

.footer{position:absolute;left:0;top:1168px;width:890px;text-align:center;font-size:8px;color:#444;word-spacing:1px}
.footer span{margin:0 10px}
</style>
</head>
<body>
<div class="topline"></div>

<header>
  <div class="brand">
    <span class="brand-mark"></span>
    <span class="brand-name">Corvana Forums</span>
  </div>
  <div class="social">
    <span class="social-label">Connect with our social network :</span>
    <span class="social-dot dot-a" aria-label="Social network 1"></span>
    <span class="social-dot dot-b" aria-label="Social network 2"></span>
    <span class="social-dot dot-c" aria-label="Social network 3"></span>
    <span class="social-dot dot-d" aria-label="Social network 4"></span>
    <span class="social-dot dot-e" aria-label="Social network 5"></span>
  </div>
</header>

<nav class="nav">
  <a>Home</a><a>About Us</a><a>Business</a><a>Politics</a><a>Entertainment</a><a>Social issues</a>
  <div class="search">Search :
    <svg width="8" height="8" viewBox="0 0 10 10"><circle cx="4" cy="4" r="3" fill="none" stroke="#999" stroke-width="1.4"/><line x1="6.3" y1="6.3" x2="9.3" y2="9.3" stroke="#999" stroke-width="1.4"/></svg>
  </div>
</nav>

<section class="hero">
  <div class="hero-media" role="img" aria-label="Night view of a lit bridge over a bay under a moonlit sky">
    <div class="hero-title">Corvana Forums</div>
    <div class="hero-sub">We are a business discussion forum</div>
    <div class="hero-arrows">
      <span><svg width="6" height="8" viewBox="0 0 6 8"><path d="M5 1 2 4l3 3" fill="none" stroke="#777"/></svg></span>
      <span><svg width="6" height="8" viewBox="0 0 6 8"><path d="M1 1l3 3-3 3" fill="none" stroke="#777"/></svg></span>
    </div>
  </div>
  <div class="hero-about">
    <div class="about-title">ABOUT</div>
    <div class="about-name">Corvana Forums</div>
    <p class="about-text">Lorem Ipsum is simply dummy text of the printing and typesetting industry. Lorem Ipsum has been the industry's standard dummy text ever since the 1500s, when an unknown printer took a galley.</p>
    <p class="about-text">when an unknown printer took a galley of type and scrambled.when an unknown printer took a galley...</p>
  </div>
</section>

<section class="welcome">
  <h1>Welcome to Corvana Forums</h1>
  <p>Simply dummy text of the printing and typesetting industry. Lorem Ipsum has been the industry's standard dummy text ever since the 1500s, when an unknown printer took a galley of type and scrambled it to make a type specimen book</p>
</section>

<section class="categories">
  <article class="category">
    <div class="cat-media m-business" role="img" aria-label="Businessman in a suit talking on a phone"></div>
    <h2 class="cat-title">Business</h2>
    <ul class="cat-list">
      <li><span class="bullet"></span>Start Your Business</li>
      <li><span class="bullet"></span>Grow Your Business</li>
      <li><span class="bullet"></span>Build Your Career</li>
      <li><span class="bullet"></span>Lead Your Team</li>
      <li><span class="bullet"></span>Find a Solution</li>
    </ul>
    <a class="view-more">View more »</a>
  </article>
  <article class="category">
    <div class="cat-media m-politics" role="img" aria-label="Woman speaking into a microphone before an audience"></div>
    <h2 class="cat-title">Politics</h2>
    <ul class="cat-list">
      <li><span class="bullet"></span>Freedom</li>
      <li><span class="bullet"></span>Geopolitics</li>
      <li><span class="bullet"></span>Direct Action</li>
      <li><span class="bullet"></span>Documentaries</li>
      <li><span class="bullet"></span>Voting</li>
    </ul>
    <a class="view-more">View more »</a>
  </article>
  <article class="category">
    <div class="cat-media m-entertain" role="img" aria-label="Band performing with a singer and guitarist"></div>
    <h2 class="cat-title">Entertainment</h2>
    <ul class="cat-list">
      <li><span class="bullet"></span>Music</li>
      <li><span class="bullet"></span>Video</li>
      <li><span class="bullet"></span>Arts &amp; Entertainment</li>
      <li><span class="bullet"></span>Artists</li>
      <li><span class="bullet"></span>Shows</li>
    </ul>
    <a class="view-more">View more »</a>
  </article>
  <article class="category">
    <div class="cat-media m-social" role="img" aria-label="Commuters walking across a bridge in golden light"></div>
    <h2 class="cat-title">Social issues</h2>
    <ul class="cat-list">
      <li><span class="bullet"></span>Poor</li>
      <li><span class="bullet"></span>Public</li>
      <li><span class="bullet"></span>Speaches</li>
      <li><span class="bullet"></span>Environment</li>
      <li><span class="bullet"></span>Traffic</li>
    </ul>
    <a class="view-more">View more »</a>
  </article>
</section>

<section class="band">
  <h2>Business, Politics, Entertainment and Social issues</h2>
  <span class="band-arrow" style="left:37px">‹</span>
  <span class="band-arrow" style="left:849px">›</span>
  <div class="feature" style="left:57px">
    <div class="feature-thumb t-1" role="img" aria-label="Colleagues working at a laptop"></div>
    <div><h3>Business</h3><p>Lorem Ipsum is simply<br>dummy printing...</p><span class="btn">CLICK HERE</span></div>
  </div>
  <div class="feature" style="left:257px">
    <div class="feature-thumb t-2" role="img" aria-label="Concert stage under blue lights"></div>
    <div><h3>Politics</h3><p>Lorem Ipsum is simply<br>dummy printing...</p><span class="btn">CLICK HERE</span></div>
  </div>
  <div class="feature" style="left:457px">
    <div class="feature-thumb t-3" role="img" aria-label="Festival crowd"></div>
    <div><h3>Culture</h3><p>Lorem Ipsum is simply<br>dummy printing...</p><span class="btn">CLICK HERE</span></div>
  </div>
  <div class="feature" style="left:657px">
    <div class="feature-thumb t-4" role="img" aria-label="Portrait of a woman"></div>
    <div><h3>History</h3><p>Lorem Ipsum is simply<br>dummy printing...</p><span class="btn">CLICK HERE</span></div>
  </div>
</section>

<footer class="footer">
  ©2016. Corvana Forums. All rights reserved.<span></span>Terms &amp; Conditions<span>/</span>Privacy Policy<span>/</span>Disclaimer
</footer>
</body>
</html>
```